Tallyleaf Web Design

Create Website Design for Tallyleaf. Tallyleaf is online application for collaboration team work system (task list management). More concept design for this project please find attach file ("tallyleaf website concept.pdf") . But my concept is just describe minimal features not bind design

For tallyleaf logo, i had already attach files. But i had not decided what color i chose, so it's okay if you suggest logo color for your suitable website design.
Updates

Dear All Designer,

I like brisk carousel (http://quorvanlabs.example/brisk-carousel/),
may be your concept design can adjust with this concept.
but don't worry about script for brisk carousel, my team will be handle
You just make website design to suitable with brisk carousel

but if you had own website design concept are welcome

thanks

Target Market(s)

Business Company

Industry/Entity Type

Management

```html
<!DOCTYPE html>
<html lang="en">
<head>
<meta charset="utf-8">
<title>Tallyleaf — Online team collaboration</title>
<link href="https://fonts.googleapis.com/css2?family=PT+Sans:wght@400;700&family=Arimo:wght@400;700&display=swap" rel="stylesheet">
<style>
:root{
  --green:#3f8a12;
  --green-dark:#1f4a06;
  --green-light:#6cc01f;
  --lime:#8fd42a;
  --nav-bg:#1d3a0c;
  --nav-text:#ffffff;
  --ink:#2a2a2a;
  --muted:#8c8c8c;
  --faint:#b4b4b4;
  --line:#dcdcdc;
  --panel:#f2f2f2;
  --panel-edge:#d4d4d4;
  --slider-frame:#5a5a5a;
  --slider-black:#0d0d0d;
  --yellow:#f5d41d;
  --blue-title:#2f77b4;
  --card-title:#4b7dae;
  --footer:#9a9a9a;
  --footer-text:#3e3e3e;
}
*{box-sizing:border-box;margin:0;padding:0}
html,body{width:1080px;height:1200px;overflow:hidden;background:#fff}
body{position:relative;font-family:"Arimo",Arial,sans-serif;color:var(--ink)}
.abs{position:absolute}

/* header */
.header-top{left:0;top:0;width:1080px;height:2px;background:#333}
.brand{left:147px;top:14px;display:flex;align-items:center;gap:8px}
.brand-name{font-family:"PT Sans",sans-serif;font-weight:700;font-size:50px;color:var(--green-light);letter-spacing:-1px;line-height:1}
.brand-dot{width:22px;height:22px;border-radius:50%;background:var(--green-light)}
.account-tab{left:769px;top:0;width:151px;height:19px;background:linear-gradient(#4d9a1a,#2f6a0c);border-radius:0 0 10px 10px;color:#fff;font-size:10px;text-align:center;line-height:18px}
.header-rule{left:0;top:76px;width:1080px;height:7px;background:linear-gradient(#1a1a1a,#3a3a3a)}
.main-nav{left:0;top:56px;width:1080px;height:27px}
.main-nav a{position:absolute;top:0;height:27px;background:linear-gradient(#2f5617,var(--nav-bg));border:1px solid #0e2104;color:var(--nav-text);text-decoration:none;font-size:13px;text-align:center;line-height:24px;border-radius:3px 3px 0 0}
.main-nav a.active{color:var(--lime)}

/* hero */
.hero{left:0;top:83px;width:1080px;height:292px;background:radial-gradient(ellipse at 50% 40%,#5fb422 0%,#3b8a12 45%,#1e5a08 100%)}
.hero-shade{left:0;top:83px;width:1080px;height:292px;background:linear-gradient(90deg,rgba(0,0,0,.18),transparent 25%,transparent 75%,rgba(0,0,0,.18))}
.slider-frame{left:149px;top:107px;width:768px;height:240px;background:linear-gradient(#8a8a8a,#3a3a3a);border-radius:6px;box-shadow:0 4px 10px rgba(0,0,0,.45)}
.slider-side{top:117px;width:52px;height:220px;background:#2a2a2a}
.slider-stage{left:217px;top:117px;width:620px;height:220px;background:var(--slider-black)}
.slider-arrow{top:201px;width:30px;height:48px;border-radius:24px;background:#1a1a1a;border:2px solid #333}
.headline{left:224px;top:133px;font-size:32px;color:#fff;white-space:nowrap;letter-spacing:-.3px}
.headline em{font-style:normal;color:var(--yellow)}
.caution-rule{left:224px;top:187px;width:600px;height:9px;background:repeating-linear-gradient(90deg,var(--yellow) 0 18px,transparent 18px 30px)}
.search{left:224px;top:213px;width:184px;height:21px;background:#3a3a3a;border:1px solid #555;color:#ddd;font-size:10px;line-height:19px;padding-left:24px}
.search-go{left:386px;top:214px;width:21px;height:19px;background:#1a1a1a;color:#fff;font-size:9px;text-align:center;line-height:19px}
.slider-btn{top:244px;height:19px;background:#2a2a2a;border-bottom:3px solid var(--yellow);color:#fff;font-size:10px;text-align:center;line-height:17px}
.news-bar{left:224px;top:267px;width:185px;height:20px;background:repeating-linear-gradient(135deg,var(--yellow) 0 8px,#111 8px 14px)}
.news-label{left:224px;top:267px;width:96px;height:20px;background:var(--yellow);font-weight:700;font-size:11px;line-height:20px;padding-left:8px;color:#111}
.news-thumb{left:230px;top:296px;width:45px;height:33px;background:linear-gradient(#6b7f99,#cfd6de)}
.news-title{left:280px;top:297px;font-size:9px;font-weight:700;color:#fff}
.news-text{left:280px;top:309px;width:128px;font-size:8px;line-height:10px;color:#bbb}
.slide-image{left:428px;top:213px;width:359px;height:131px;background:linear-gradient(100deg,#b92a1e 0%,#2b4f8e 35%,#e6e6ea 60%,#b9262a 100%)}
.pager{left:803px;top:215px}
.pager span{display:block;width:17px;height:16px;margin-bottom:5px;background:#fff;color:#111;font-size:10px;text-align:center;line-height:16px}
.pager span.on{background:var(--yellow)}

/* tabs */
.tab{top:385px;width:208px;height:68px;background:linear-gradient(#f3f3f3,#d9d9d9);border:1px solid #c4c4c4;border-bottom:none}
.tab.on{background:#fff;border-color:#cfcfcf;height:70px}
.tab-icon{position:absolute;left:14px;top:14px}
.tab-title{position:absolute;left:64px;top:22px;font-family:"PT Sans",sans-serif;font-weight:700;font-size:16px;color:#a9a9a9}
.tab.on .tab-title{color:var(--blue-title)}
.tab-sub{position:absolute;left:64px;top:42px;font-size:9px;color:#c4c4c4}
.tab.on .tab-sub{color:#9a9a9a}
.tab-rule{left:149px;top:453px;width:768px;height:1px;background:var(--line)}

/* features */
.feature{left:149px;width:443px;height:40px;background:linear-gradient(90deg,#f7f7f7,#fff 60%,#f3f3f3);border:1px solid #e4e4e4;border-radius:4px}
.feature svg{position:absolute;left:10px;top:13px}
.feature p{position:absolute;left:34px;top:7px;width:300px;font-size:10px;line-height:14px;color:var(--faint)}
.feature .more{position:absolute;left:344px;top:7px;width:84px;height:24px;background:#f0f0f0;border:1px solid #e2e2e2;font-size:10px;color:#c0c0c0;text-align:center;line-height:22px}

/* signup */
.field{height:24px;border:1px solid #cfcfcf;font-size:13px;color:#333;line-height:22px;padding-left:10px;background:#fff}
.signup{left:667px;top:560px;width:218px;height:35px;border-radius:4px;background:linear-gradient(#7bd02a,#3d9a10);box-shadow:0 2px 3px rgba(0,0,0,.3);color:#fff;font-weight:700;font-size:14px;text-align:center;line-height:35px}
.team-panel{left:629px;top:623px;width:288px;height:220px;background:linear-gradient(#f6f6f6,#e9e9e9);border:1px solid var(--panel-edge);border-radius:4px}
.team-head{left:643px;top:635px;width:261px;height:35px;background:#f8f8f8;border:1px solid #dedede;font-family:"PT Sans",sans-serif;font-size:19px;color:#8a8a8a;line-height:33px;padding-left:12px}
.team-tile{width:61px;height:60px;background:linear-gradient(#fbfbfb,#e4e4e4);border:1px solid #d2d2d2;border-radius:3px;display:flex;align-items:center;justify-content:center}

/* article */
.article-title{left:152px;top:716px;font-family:"PT Sans",sans-serif;font-size:22px;color:#2f6d10}
.article-art{left:149px;top:753px;width:218px;height:167px;background:radial-gradient(ellipse at 50% 60%,#c7d2dc 0%,#e9eef2 55%,#fff 80%)}
.article-text{left:375px;top:755px;width:218px;font-size:11px;line-height:16.8px;color:#444;text-align:justify}

/* blog */
.blog-band{left:0;top:956px;width:1080px;height:211px;background:linear-gradient(#e6e6e6,#f2f2f2 30%,#cfcfcf);border-top:1px solid #d0d0d0}
.blog-heading{left:284px;top:978px;font-family:"PT Sans",sans-serif;font-size:17px;color:#b2b2b2}
.blog-rule{left:195px;top:1004px;width:682px;height:1px;background:#d2d2d2}
.blog-card{top:1024px;height:105px;background:#fff;border:1px solid #d6d6d6}
.blog-card h3{position:absolute;left:17px;top:8px;font-family:"PT Sans",sans-serif;font-weight:700;font-size:13px;color:var(--card-title)}
.blog-card p{position:absolute;left:17px;top:28px;width:240px;font-size:8.5px;line-height:13px;color:#c4c4c4}
.blog-card .meta{position:absolute;left:17px;top:86px;font-size:9px;color:#999;display:flex;gap:6px;align-items:center}
.blog-card .more{position:absolute;right:10px;top:74px;width:84px;height:25px;background:#f1f1f1;border:1px solid #e0e0e0;font-size:10px;color:#b8b8b8;text-align:center;line-height:23px}

/* footer */
.footer{left:0;top:1167px;width:1080px;height:33px;background:linear-gradient(#b3b3b3,#8f8f8f)}
.footer-links{left:195px;top:1177px;font-size:10px;color:var(--footer-text);word-spacing:2px}
.copyright{left:711px;top:1177px;font-size:10px;color:var(--footer-text)}
</style>
</head>
<body>

<!-- header -->
<div class="abs header-top"></div>
<div class="abs brand"><span class="brand-name">tallyleaf</span><span class="brand-dot"></span></div>
<div class="abs account-tab">Plans &amp; Pricing &nbsp;|&nbsp; Sign in</div>
<div class="abs header-rule"></div>
<nav class="abs main-nav">
  <a class="active" style="left:430px;width:74px" href="#">Products</a>
  <a style="left:515px;width:74px" href="#">Solutions</a>
  <a style="left:597px;width:75px" href="#">Industries</a>
  <a style="left:677px;width:75px" href="#">Webinars</a>
  <a style="left:759px;width:80px" href="#">About Us</a>
  <a style="left:843px;width:74px" href="#">Contact Us</a>
</nav>

<!-- hero carousel -->
<div class="abs hero"></div>
<div class="abs hero-shade"></div>
<div class="abs slider-frame"></div>
<div class="abs slider-side" style="left:165px"></div>
<div class="abs slider-side" style="left:837px"></div>
<div class="abs slider-stage"></div>
<div class="abs slider-arrow" style="left:160px"><svg width="26" height="44" viewBox="0 0 26 44"><path d="M16 16l-6 6 6 6" stroke="#fff" stroke-width="3" fill="none"/></svg></div>
<div class="abs slider-arrow" style="left:876px"><svg width="26" height="44" viewBox="0 0 26 44"><path d="M10 16l6 6-6 6" stroke="#fff" stroke-width="3" fill="none"/></svg></div>
<div class="abs headline"><em>Online team</em> collaboration to get work done.</div>
<div class="abs caution-rule"></div>
<div class="abs search">SEARCH</div>
<svg class="abs" style="left:229px;top:217px" width="13" height="13" viewBox="0 0 13 13"><circle cx="5" cy="5" r="3.8" stroke="#ccc" stroke-width="1.6" fill="none"/><path d="M8 8l4 4" stroke="#ccc" stroke-width="1.8"/></svg>
<div class="abs search-go">GO</div>
<div class="abs slider-btn" style="left:224px;width:88px">Sign In</div>
<div class="abs slider-btn" style="left:321px;width:88px">Create account</div>
<div class="abs news-bar"></div>
<div class="abs news-label">Latest News</div>
<div class="abs news-thumb" role="img" aria-label="Small news photo of a person at a desk"></div>
<div class="abs news-title">Lorem ipsum dolo</div>
<div class="abs news-text">Lorem ipsum dolor sit amet. Sed elementum molestie</div>
<div class="abs slide-image" role="img" aria-label="Photo of hands using a tablet showing a document app on a red table"></div>
<div class="abs pager"><span class="on">1</span><span>2</span><span>3</span><span>4</span><span>5</span><span>6</span></div>

<!-- tabs -->
<div class="abs tab on" style="left:149px">
  <svg class="tab-icon" width="40" height="40" viewBox="0 0 40 40"><circle cx="14" cy="13" r="6" fill="#6a8fb8"/><rect x="5" y="21" width="18" height="15" rx="6" fill="#2f5f96"/><circle cx="27" cy="17" r="5" fill="#7fbf3a"/><rect x="19" y="24" width="16" height="12" rx="5" fill="#3d8a17"/></svg>
  <div class="tab-title">EXPERIENCE</div><div class="tab-sub">professionals working together</div>
</div>
<div class="abs tab" style="left:429px">
  <svg class="tab-icon" width="40" height="40" viewBox="0 0 40 40"><rect x="5" y="7" width="30" height="20" rx="2" fill="#9a9a9a"/><rect x="8" y="10" width="24" height="14" fill="#d4d4d4"/><rect x="16" y="27" width="8" height="5" fill="#8a8a8a"/><rect x="11" y="32" width="18" height="3" fill="#9a9a9a"/></svg>
  <div class="tab-title">TECHNOLOGIES</div><div class="tab-sub">we use only the best stuff</div>
</div>
<div class="abs tab" style="left:709px">
  <svg class="tab-icon" width="40" height="40" viewBox="0 0 40 40"><path d="M8 34L24 18" stroke="#9a9a9a" stroke-width="6" stroke-linecap="round"/><circle cx="28" cy="13" r="8" fill="#a8a8a8"/><path d="M28 8l5 5" stroke="#efefef" stroke-width="4"/></svg>
  <div class="tab-title">SUPPORT</div><div class="tab-sub">24/7 user satisfaction</div>
</div>
<div class="abs tab-rule"></div>

<!-- features -->
<div class="abs feature" style="top:483px"><svg width="14" height="12" viewBox="0 0 14 12"><path d="M1 6l4 4 8-9" stroke="#5aa72a" stroke-width="2.6" fill="none"/></svg><p>Lorem ipsum dolor sit amet,consectetur adipiscing elit.ipsum dolor sit amet,consectetur adipiscing elit.</p><span class="more">Read more</span></div>
<div class="abs feature" style="top:540px"><svg width="14" height="12" viewBox="0 0 14 12"><path d="M1 6l4 4 8-9" stroke="#5aa72a" stroke-width="2.6" fill="none"/></svg><p>Lorem ipsum dolor sit amet,consectetur adipiscing elit.ipsum dolor sit amet,consectetur adipiscing elit.</p><span class="more">Read more</span></div>
<div class="abs feature" style="top:596px"><svg width="14" height="12" viewBox="0 0 14 12"><path d="M1 6l4 4 8-9" stroke="#5aa72a" stroke-width="2.6" fill="none"/></svg><p>Lorem ipsum dolor sit amet,consectetur adipiscing elit.ipsum dolor sit amet,consectetur adipiscing elit.</p><span class="more">Read more</span></div>
<div class="abs feature" style="top:653px"><svg width="14" height="12" viewBox="0 0 14 12"><path d="M1 6l4 4 8-9" stroke="#5aa72a" stroke-width="2.6" fill="none"/></svg><p>Lorem ipsum dolor sit amet,consectetur adipiscing elit.ipsum dolor sit amet,consectetur adipiscing elit.</p><span class="more">Read more</span></div>

<!-- signup -->
<div class="abs field" style="left:631px;top:469px;width:286px">Email</div>
<div class="abs field" style="left:631px;top:507px;width:132px">Confirm passward</div>
<div class="abs field" style="left:781px;top:507px;width:136px">Confirm passward</div>
<div class="abs signup">SIGN UP NOW FOR FREE</div>

<div class="abs team-panel"></div>
<div class="abs team-head">Team Works</div>
<div class="abs team-tile" style="left:651px;top:689px"><svg width="26" height="26" viewBox="0 0 26 26"><circle cx="13" cy="13" r="10" fill="none" stroke="#777" stroke-width="5"/><circle cx="13" cy="13" r="10" fill="none" stroke="#e7e7e7" stroke-width="5" stroke-dasharray="6 9.7"/></svg></div>
<div class="abs team-tile" style="left:744px;top:689px"><svg width="24" height="26" viewBox="0 0 24 26"><rect x="3" y="2" width="18" height="22" rx="2" fill="#666"/><rect x="5" y="4" width="3" height="18" fill="#999"/><circle cx="14" cy="13" r="3.5" fill="none" stroke="#ddd" stroke-width="1.5"/></svg></div>
<div class="abs team-tile" style="left:836px;top:689px"><svg width="26" height="26" viewBox="0 0 26 26"><path d="M5 21l2-6 12-12 4 4-12 12z" fill="#666"/><path d="M5 21l2-6 4 4z" fill="#bbb"/></svg></div>
<div class="abs team-tile" style="left:651px;top:769px"><svg width="28" height="26" viewBox="0 0 28 26"><rect x="2" y="3" width="24" height="15" rx="1" fill="#888"/><rect x="4" y="5" width="20" height="11" fill="#d8d8d8"/><rect x="11" y="18" width="6" height="3" fill="#888"/><rect x="8" y="21" width="12" height="2" fill="#999"/></svg></div>
<div class="abs team-tile" style="left:744px;top:769px"><svg width="28" height="26" viewBox="0 0 28 26"><rect x="2" y="3" width="24" height="19" fill="#cfcfcf" stroke="#999"/><path d="M4 19l6-7 5 4 8-9" stroke="#888" stroke-width="2" fill="none"/></svg></div>
<div class="abs team-tile" style="left:836px;top:769px"><svg width="24" height="24" viewBox="0 0 24 24"><rect x="2" y="2" width="20" height="20" rx="2" fill="#444"/><rect x="6" y="2" width="12" height="7" fill="#ddd"/><rect x="5" y="13" width="14" height="9" fill="#eee"/></svg></div>

<!-- article -->
<h2 class="abs article-title">Lorem ipsum dolor sit amet</h2>
<div class="abs article-art" role="img" aria-label="Illustration of team members connected in a collaboration network"></div>
<p class="abs article-text">There are many variations of passages of Lorem Ipsum available, but the majority have suffered alteration in some form, by injected humour, or randomised words which don't look even slightly believable. If you are going to use a passage of Lorem Ipsum, you need to be sure there isn't anything embarrassing hidden in the middle of text. There are many variations of passages of Lorem Ipsum available, but the majority have suffered alteration in some form, by injected</p>

<!-- blog -->
<div class="abs blog-band"></div>
<svg class="abs" style="left:245px;top:974px" width="28" height="26" viewBox="0 0 28 26"><path d="M3 6l14-4 8 14-14 6z" fill="#9a9a9a"/><path d="M3 6l8 16" stroke="#777" stroke-width="2"/></svg>
<div class="abs blog-heading">Latest News On Blog</div>
<div class="abs blog-rule"></div>
<article class="abs blog-card" style="left:209px;width:248px">
  <h3>Lorem ipsum dolor sit amet, consectetur</h3>
  <p>In semper sodales felis, eu egestas nisi dignissim quis. Mauris vitae eros elit, vitae egestas magna. Donec ac mi lorem. Ut arcu dui, eleifend vel auctor a, tincidunt eu tortor.</p>
  <div class="meta"><svg width="11" height="10" viewBox="0 0 11 10"><rect width="11" height="7" rx="1" fill="#aaa"/><path d="M2 7v3l3-3z" fill="#aaa"/></svg>14 comments</div>
  <span class="more">Read more</span>
</article>
<article class="abs blog-card" style="left:577px;width:286px">
  <h3>Lorem ipsum dolor sit amet.</h3>
  <p>In semper sodales felis, eu egestas nisi dignissim quis. Mauris vitae eros elit, vitae egestas magna. Donec ac mi lorem. Ut arcu dui, eleifend vel auctor a, tincidunt eu tortor.</p>
  <div class="meta"><svg width="11" height="10" viewBox="0 0 11 10"><rect width="11" height="7" rx="1" fill="#aaa"/><path d="M2 7v3l3-3z" fill="#aaa"/></svg>16 comments</div>
  <span class="more">Read more</span>
</article>

<!-- footer -->
<div class="abs footer"></div>
<div class="abs footer-links">Home &nbsp;|&nbsp; Portfolio &nbsp;|&nbsp; Services &nbsp;|&nbsp; About &nbsp;|&nbsp; Testimonials &nbsp;|&nbsp; Contacts &nbsp;|&nbsp; Blogs</div>
<div class="abs copyright">Copyright © 2013 ..............</div>

</body>
</html>
```